Velmora Outcomes WebDesign

Although the designs we have had are great we are looking for something unique and would like to move away from the traditional. We append additional comments and files to reflect this. WE are looking for designs to showcase there artistic flare.

Task
To design Velmora Outcomes home page and a second page ie information on our Internet Marketing Services

Client:
Velmora Outcomes is the next generation provider of international marketing, branding, design, Search Engine Optimization(SEO) and Search Engine Marketing(SEM). Utilising a variety of crowd-source channels and trust networks, Velmora Outcomes is able to offer you a complete internet marketing package. From initial design and branding to the continued work on SEO all our services are geared towards dramatically increasings your revenues. Our primary goal is to build greater trading bridges between English-speaking and Chinese-speaking worlds. We believe that a true understanding of the local market is only achievable if you are a native speaker. The power of our networks and processes have been focused to enable Velmora Outcomes to enlist only native speakers to bolster your Internet Marketing Campaign.

The primary color pallet is:

FF9571
B23308
FF6633
858585
BDBDBD
or
https://tintpick.example.com/#themes/search?term=velmora%20outcomes

Sites we like
http://www.brontavix.com/
http://www.quelmaro.com/
Updates

We have believe that we will need to push our design packages (outsourced through artflock) more. We would like this to be reflected on the front page.

This means that the menu should also include

Design
Also the use of content management system joomla

Have added a few more sites that we like
www.harbourpixelcraft.com.hk
www.qmv.hk

Really excited with all the designs so far.  We would like the design to move away from the more standard layout. With this in mind we would like to see some design that feature hexagons, or decagons.
Please feel free to let loose! we want a design that is quit unique

We have included to vector files.

vector file 8016151 is for a color reference we thik that in order to enhence the design we need to expand the color palette, would want to maintain the primary corporate colors, but include some bright additional colors.

The second was our insipration for the the hexagon. expanding on the idea we thought that the main menu could be made up of hexagons. The ad/info modules that appear half way up the page be similar to those in the vector.

Reason: Have updated brief and are looking for a more unique feel to the design.

Target Market(s)

Small to medium business looking to branch out further in the international market

Industry/Entity Type

Internet

Requirements
Must have
• A login/search section
A separate floating feedback tab
Main Navigation – Home, Internet Marketing, Cloud Computing
A banner space from informative text on our services
Must have a request for a quote on each page

```html
<!DOCTYPE html>
<html lang="en">
<head>
<meta charset="utf-8">
<title>Velmora Outcomes – SEO Experts</title>
<link href="https://fonts.googleapis.com/css2?family=Ubuntu:wght@400;500;700&family=Arimo:wght@400;700&display=swap" rel="stylesheet">
<style>
:root{
  --orange:#f26522;
  --orange-light:#ff9571;
  --orange-deep:#e0521a;
  --red-shadow:#b23308;
  --charcoal:#333333;
  --grey-text:#858585;
  --grey-soft:#bdbdbd;
  --green-dark:#0b5a26;
  --green-lime:#9ccc32;
  --link-blue:#1b6fa6;
  --page-bg:#f5f5f5;
  --white:#ffffff;
}
*{margin:0;padding:0;box-sizing:border-box}
html,body{width:1200px;height:1129px;overflow:hidden}
body{position:relative;background:var(--page-bg);font-family:"Arimo",Arial,sans-serif;color:#666}

/* header */
.site-header{position:absolute;left:0;top:0;width:1200px;height:113px;background:linear-gradient(#2a2a2a,#3a3a3a)}
.site-header::before{content:"";position:absolute;left:0;top:0;width:100%;height:3px;background:var(--orange)}
.brand{position:absolute;left:113px;top:10px;display:flex;align-items:center;gap:18px}
.brand-mark{width:50px;height:50px;border-radius:50%;border:4px solid var(--orange)}
.brand-name{font-family:"Ubuntu",sans-serif;font-weight:700;font-size:26px;color:var(--orange);line-height:1}
.brand-tag{display:block;font-family:"Ubuntu",sans-serif;font-size:8px;color:#aaa;margin-top:4px;padding-left:24px}
.account-links{position:absolute;left:954px;top:2px;display:flex;font-family:"Ubuntu",sans-serif;font-size:13px}
.account-links a{display:block;height:24px;line-height:24px;padding:0 7px;color:var(--white);text-decoration:none}
.account-links .login{background:var(--orange)}
.main-nav{position:absolute;left:110px;top:70px;width:966px;height:41px;background:linear-gradient(#f77a38,var(--orange-deep));display:flex;align-items:center}
.main-nav a{font-family:"Ubuntu",sans-serif;font-size:13px;color:var(--white);text-decoration:none;letter-spacing:.4px;height:41px;line-height:41px}
.main-nav .home{background:#d4501a;padding:0 20px;margin-left:7px;margin-right:14px}
.main-nav .item{margin-right:27px}
.nav-search{position:absolute;left:674px;top:6px;width:290px;height:30px;background:var(--white);border-radius:15px;box-shadow:0 0 0 2px #f9b08c inset}
.nav-search span{position:absolute;left:8px;top:7px;width:216px;height:17px;border:1px solid #ddd;border-radius:3px;font-size:7px;color:#aaa;font-style:italic;line-height:15px;padding-left:5px;font-family:"Arimo",sans-serif}
.nav-search b{position:absolute;left:230px;top:7px;width:50px;height:17px;background:var(--orange);border-radius:3px;color:var(--white);font-size:8px;font-weight:400;text-align:center;line-height:17px;font-family:"Arimo",sans-serif}

/* hero */
.hero{position:absolute;left:0;top:113px;width:1200px;height:297px;background:radial-gradient(ellipse 520px 420px at 620px 40px,#a6d43a 0%,#7fbf2e 40%,#2f8a2a 70%,var(--green-dark) 100%);border-top:3px solid var(--orange)}
.hero h1{position:absolute;left:118px;top:18px;font-family:"Ubuntu",sans-serif;font-weight:700;font-size:58px;color:var(--white);letter-spacing:.5px}
.hero p{position:absolute;left:122px;top:90px;font-family:"Ubuntu",sans-serif;font-size:17.5px;color:var(--white)}

.service-hexes{position:absolute;left:105px;top:244px;width:1000px;height:255px}
.hex{position:absolute;top:0;width:260px;height:255px}
.hex svg{position:absolute;left:0;top:0}
.hex-label{position:absolute;left:40px;width:150px;text-align:center;font-family:"Arimo",sans-serif;font-weight:700;font-size:11px;line-height:13px;color:var(--orange-deep)}

/* content */
.content-panel{position:absolute;left:58px;top:527px;width:1064px;height:445px;background:var(--white)}
.section-title{font-family:"Ubuntu",sans-serif;font-weight:700;font-size:22px;color:var(--orange)}
.services{position:absolute;left:81px;top:11px}
.services ul{list-style:none;margin-top:20px}
.services li{font-family:"Ubuntu",sans-serif;font-weight:500;font-size:12.5px;color:var(--link-blue);height:25px;line-height:25px;padding-left:14px;position:relative}
.services li::before{content:"";position:absolute;left:0;top:10px;border-left:4px solid var(--link-blue);border-top:3px solid transparent;border-bottom:3px solid transparent}
.welcome{position:absolute;left:272px;top:11px;width:336px}
.welcome .section-title{font-size:21px}
.welcome .intro{margin-top:15px;font-size:12px;line-height:14.2px;color:#777}
.welcome hr{border:0;border-top:1px solid #ddd;margin:10px 0 14px;width:326px}
.welcome .aside{font-size:12px;line-height:16px;color:#999;padding-left:2px;width:326px}
.more-link{display:block;text-align:right;margin-top:13px;width:322px;font-family:"Ubuntu",sans-serif;font-weight:500;font-size:10px;color:var(--link-blue);text-decoration:none}
.welcome-fade{position:absolute;left:255px;top:363px;width:390px;height:76px;background:#fafafa}
.featured{position:absolute;left:661px;top:11px;width:312px}
.featured .section-title{display:flex;align-items:center;gap:8px}
.featured .rss{width:14px;height:14px;border-radius:2px;background:var(--orange-light)}
.project-name{font-family:"Arimo",sans-serif;font-weight:700;font-size:12.5px;color:#111}
.project-thumb{width:310px;height:121px;border-radius:14px;margin-top:8px}
.thumb-one{background:linear-gradient(#f6f6f6,#d8d8d8 60%,#f0f0f0)}
.thumb-two{background:linear-gradient(#f6e8b8 0%,#f1dfa0 32%,#c2762a 38%,#b96b22 100%)}
.view-link{display:block;text-align:right;font-family:"Ubuntu",sans-serif;font-weight:500;font-size:10px;color:var(--link-blue);text-decoration:none}

/* footer */
.site-footer{position:absolute;left:0;top:972px;width:1200px;height:157px;background:radial-gradient(ellipse 500px 300px at 620px 60px,#a6d43a 0%,#7fbf2e 40%,#2f8a2a 70%,var(--green-dark) 100%)}
.site-footer::before{content:"";position:absolute;left:0;top:7px;width:1186px;height:4px;background:var(--orange)}
.footer-brand{position:absolute;left:160px;top:22px;display:flex;align-items:center;gap:12px}
.footer-brand .brand-mark{width:32px;height:32px;border-width:3px}
.footer-brand .brand-name{font-size:17px}
.rights{position:absolute;left:199px;top:61px;font-family:"Arimo",sans-serif;font-weight:700;font-size:10px;color:var(--white)}
.social{position:absolute;left:910px;top:35px;display:flex;gap:7px}
.social span{width:19px;height:19px;border-radius:3px}
</style>
</head>
<body>

<header class="site-header">
  <div class="brand">
    <span class="brand-mark"></span>
    <div><span class="brand-name">Velmora Outcomes</span><span class="brand-tag">SEO and Cloud Consultant</span></div>
  </div>
  <nav class="account-links"><a class="login" href="#">LOGIN</a><a href="#">FEEDBACK</a></nav>
  <nav class="main-nav">
    <a class="home" href="#">HOME</a>
    <a class="item" href="#">OUR&nbsp; SERVICES</a>
    <a class="item" href="#">INTERNET MARKETING</a>
    <a class="item" href="#">COLOUD COMPUTING</a>
    <a class="item" href="#">CONTACT US</a>
    <div class="nav-search"><span>Type here</span><b>Search</b></div>
  </nav>
</header>

<section class="hero">
  <h1>Seo Experts</h1>
  <p>Our primary goal is to build greater trading bridges between English-speaking and Chinese-speaking worlds.</p>
</section>

<div class="service-hexes">
  <div class="hex" style="left:0">
    <svg width="260" height="255" viewBox="0 0 260 255">
      <defs><linearGradient id="hexFill" x1="0" y1="0" x2="1" y2="1"><stop offset="0" stop-color="#ffb347"/><stop offset="1" stop-color="#f05a1e"/></linearGradient></defs>
      <polygon points="80,10 190,10 250,125 190,240 80,240 20,125" fill="#c8361a"/>
      <polygon points="68,5 172,5 230,120 172,240 68,240 5,120" fill="url(#hexFill)"/>
      <polygon points="82,38 160,38 202,120 160,205 82,205 40,120" fill="#fff"/>
    </svg>
    <div role="img" aria-label="Business figures beside a rising bar chart" style="position:absolute;left:85px;top:72px;width:62px;height:72px;border-radius:6px;background:linear-gradient(135deg,#3a7bd5,#f7b733,#e94b3c)"></div>
    <div class="hex-label" style="left:45px;top:163px">INTERNATIONAL<br>MARKETING</div>
  </div>
  <div class="hex" style="left:248px">
    <svg width="260" height="255" viewBox="0 0 260 255">
      <polygon points="80,10 190,10 250,125 190,240 80,240 20,125" fill="#c8361a"/>
      <polygon points="68,5 172,5 230,120 172,240 68,240 5,120" fill="url(#hexFill)"/>
      <polygon points="82,38 160,38 202,120 160,205 82,205 40,120" fill="#fff"/>
    </svg>
    <div role="img" aria-label="Brochure and tablet branding mock-ups" style="position:absolute;left:68px;top:76px;width:100px;height:65px;border-radius:4px;background:linear-gradient(135deg,#dfe7ee,#f08a3c 60%,#333)"></div>
    <div class="hex-label" style="left:45px;top:166px">BRANDING,<br>DESIGN</div>
  </div>
  <div class="hex" style="left:491px">
    <svg width="260" height="255" viewBox="0 0 260 255">
      <polygon points="80,10 190,10 250,125 190,240 80,240 20,125" fill="#c8361a"/>
      <polygon points="68,5 172,5 230,120 172,240 68,240 5,120" fill="url(#hexFill)"/>
      <polygon points="82,38 160,38 202,120 160,205 82,205 40,120" fill="#fff"/>
    </svg>
    <div role="img" aria-label="Magnifying glass over a search symbol with SEO lettering" style="position:absolute;left:80px;top:60px;width:100px;height:92px;border-radius:50%;background:radial-gradient(circle,#6fa9d8,#1d5c99 70%,#fff 71%)"></div>
    <div class="hex-label" style="left:40px;top:160px">SEARCH ENGINE<br>OPTIMIZATION(SEO)</div>
  </div>
  <div class="hex" style="left:730px">
    <svg width="260" height="255" viewBox="0 0 260 255">
      <polygon points="80,10 190,10 250,125 190,240 80,240 20,125" fill="#c8361a"/>
      <polygon points="68,5 172,5 230,120 172,240 68,240 5,120" fill="url(#hexFill)"/>
      <polygon points="82,38 160,38 202,120 160,205 82,205 40,120" fill="#e9e9ec"/>
    </svg>
    <div role="img" aria-label="Word cloud of search marketing terms" style="position:absolute;left:55px;top:82px;width:125px;height:52px;border-radius:8px;background:linear-gradient(135deg,#c7283a,#7b7b7b 55%,#4a4a4a)"></div>
    <div class="hex-label" style="left:42px;top:158px">SEARCH ENGINE<br>MARKETING(SEM).</div>
  </div>
</div>

<main class="content-panel">
  <section class="services">
    <h2 class="section-title">Services:</h2>
    <ul>
      <li>Keyword Research</li><li>Pay Per Click</li><li>Link Building</li><li>Reporting</li>
      <li>Website Submissions</li><li>Sample Press Release</li><li>Testimonials</li>
      <li>Site Questionnaire</li><li>Blog</li><li>Optimization Tools</li><li>Meta Tag</li><li>Internet Marketing</li>
    </ul>
  </section>

  <div class="welcome-fade"></div>
  <section class="welcome">
    <h2 class="section-title">Welcome to Velmora Outcomes</h2>
    <p class="intro">Velmora Outcomes is the next generation provider of international marketing, branding, design, Search Engine Optimization(SEO) and Search Engine Marketing(SEM). Utilising a variety of crowd-source channels and trust networks, Velmora Outcomes is able to offer you a complete internet marketing package. From initial design and branding to the continued work on SEO all our services are geared towards dramatically increasing your revenues. Our primary goal is to build greater trading bridges between English-speaking and Chinese-speaking worlds. We believe that a true understanding of the local market is only achievable if you are a native speaker. The power of our networks and processes have been focused to enable Velmora Outcomes to enlist only native speakers to bolster your Internet Marketing Campaign.</p>
    <hr>
    <p class="aside">Mauris vel tortor vitae nibh condimentum auctor. Integer ac lacus. Cum sociis natoque penatibus et magnis dis parturient montes ascetur ridiculus mus. In purus ante ornare.</p>
    <a class="more-link" href="#">READ MORE ▸</a>
  </section>

  <section class="featured">
    <h2 class="section-title">Featured projects <span class="rss"></span></h2>
    <p class="project-name" style="margin-top:17px">Project name:</p>
    <div class="project-thumb thumb-one" role="img" aria-label="Real estate supplier website preview with city skyline"></div>
    <a class="view-link" href="#" style="margin-top:30px">VIEW PROJECT ▸</a>
    <p class="project-name" style="margin-top:-1px;padding-left:3px">Project name:</p>
    <div class="project-thumb thumb-two" role="img" aria-label="Food jar shop website preview with product photos"></div>
    <a class="view-link" href="#" style="margin-top:11px">VIEW PROJECT ▸</a>
  </section>
</main>

<footer class="site-footer">
  <div class="footer-brand"><span class="brand-mark"></span><span class="brand-name">Velmora Outcomes</span></div>
  <p class="rights">ALL RIGHTS RESERVED.</p>
  <div class="social">
    <span style="background:#1f74c4" role="img" aria-label="Professional network link"></span>
    <span style="background:#3ab0e8" role="img" aria-label="Microblog link"></span>
    <span style="background:#f28a1c" role="img" aria-label="Feed link"></span>
    <span style="background:#3aa84a" role="img" aria-label="Bookmarking link"></span>
  </div>
</footer>

</body>
</html>
```